Verpackungsdesign für Pasta aus Buchweizen
Zielgruppe
Unser Unternehmen KORNIVA sucht ein sehr modernes Verpackungsdesign für Pasta aus Buchweizen.
Unsere Produkte sind in unserem Online Shop und unterscheiden sich durch die herkömmliche Pasta, da wir Buchweizen in die Verarbeitung mit aufnehmen und somit die gesundheitsfördernde Eigenschaft des Buchweizens im Vordergrund steht. Unsere Pasta aus Buchweizenmehl mit klassischem Hartweizengrieß ist in dieser Form noch nicht im stationären Handel erhältlich, deshalb wünschen wir uns ein neues, ansprechendes Verpackungsdesign welches von den Massenprodukten aus den Regalen im Handel heraussticht. Das Design sollte also minimalistisch und sehr modern wirken, und sich deutlich von der Konkurrenz abheben.
Die Zielgruppe richtet sich sowohl an Massen die Pasta in allen Variationen lieben, als auch an ernährungsbewusste Veganer/Vegetarier die Alternativen im Bereich der herkömmlichen Pasta Kochkultur suchen.
PS: Mit dem Verkauf unserer Pasta investieren wir außerdem in den Aufbau und der Infrastruktur des Erzeugerlandes. Durch unser Prinzip „Teilen & Wachsen“ fördern wir mit unseren Gewinnen nachhaltige Projekte in den Erzeugerländern und helfen somit wirtschaftlich benachteiligten Regionen auf der Welt. (Fair Trade)
Aufgabenstellung
Wir besitzen bereits ein Logo und Verpackungen für unsere Pasta Sorten. Das Logo und das Grundgerüst der Stanzform / Verpackungsmaße (inkl. Sichtfenster) soll beibehalten werden (Siehe Anhang). Als Pasta Verpackungen benutzen wir Faltschachteln und Banderolen.
Verpackungsmaße:
- Faltschachtel (90 x 40 x 165 mm)
- Banderole (560 x 70mm)
Der Produktname ist je nach Sorte zu präzisieren:
- Fusilli
- Makkaroni
- Bandnudeln
- Tarhana
Produktgewicht:
- 250g
Eigenschaften:
- Buchweizenmehl
- 100% Vegan
- Kochzeit 3 Minuten
- Liebevolle Handarbeit
WICHTIG:
1) Bitte benutzt die hochgeladene, leere Stanzform für Artwork.
2) Die Designfarbe kann anhand des Aufstellers ausgerichtet werden (CMYK: 0, 20, 32, 0 und 60, 57, 56, 62) es ist aber kein muss und ihr seit frei in der Kreativität.
3) Bitte das Sichtfenster mit Rand wie aktuell auf den Produkten übernehmen (siehe www.korniva.de/shop)
Nach dem Wettbewerb planen wir zusätzlich ein 1zu1 Projekt und würden uns freuen einen Gewinner auszuwählen - Wir freuen uns auf eure Ideen :)

```html
<!DOCTYPE html>
<html lang="de">
<head>
<meta charset="utf-8">
<title>KORNIVA Fusilli – Faltschachtel Vorderseiten</title>
<link href="https://fonts.googleapis.com/css2?family=Tinos:wght@400;700&family=Roboto:wght@400&display=swap" rel="stylesheet">
<style>
  :root {
    --stage-light: #d6d6d6;
    --stage-dark: #330508;
    --cream: #f6dfb6;
    --navy-top: #2b4f86;
    --navy-mid: #163a72;
    --navy-deep: #0f2a5e;
    --navy-label: #1d2f74;
    --navy-wave: #1a2868;
    --umber-top: #6b625c;
    --umber-base: #3b2e28;
    --umber-label: #8a6a47;
    --umber-label-deep: #6e4c2a;
    --umber-circle: #a6835f;
    --pasta: #e0a53b;
    --pasta-deep: #9a6a3a;
    --veg-mix: #8f9a62;
    --veg-warm: #c9a66e;
  }
  * { box-sizing: border-box; margin: 0; padding: 0; }
  html, body { width: 943px; height: 1200px; overflow: hidden; background: var(--stage-light); }
  .canvas {
    position: relative; width: 943px; height: 1200px;
    background: linear-gradient(180deg, var(--stage-light) 0 600px, var(--stage-dark) 600px 100%);
  }

  .box-front {
    position: absolute; left: 294px; width: 354px; height: 580px; overflow: hidden;
  }
  .box-front--navy { top: 10px; background: linear-gradient(160deg, var(--navy-top) 0%, var(--navy-mid) 35%, var(--navy-deep) 100%); }
  .box-front--umber { top: 610px; background: linear-gradient(180deg, var(--umber-top) 0%, var(--umber-base) 60%, #2c2420 100%); }

  .label-band { position: absolute; left: 0; right: 0; top: 88px; height: 430px; }
  .box-front--navy .label-band { background: var(--navy-label); }
  .box-front--umber .label-band { background: linear-gradient(180deg, var(--umber-label) 0%, var(--umber-label-deep) 100%); }

  .label-frame {
    position: absolute; left: 10px; right: 6px; top: 100px; height: 406px;
    border: 3px solid var(--cream); overflow: hidden;
  }

  .brand {
    position: absolute; left: 0; right: 0; top: 54px; text-align: center;
    font-family: "Tinos", serif; font-weight: 700; font-size: 30px; letter-spacing: 1px;
    color: var(--cream); z-index: 2;
  }
  .box-front--umber .brand { right: 40px; }

  .product-name { position: absolute; font-family: "Tinos", serif; color: var(--cream); z-index: 2; }
  .box-front--navy .product-name { left: 0; right: 0; top: 138px; text-align: center; font-size: 38px; font-weight: 400; }
  .box-front--umber .product-name { left: 14px; top: 150px; font-size: 34px; font-weight: 700; }

  .properties { position: absolute; font-family: "Tinos", serif; color: var(--cream); list-style: none; z-index: 2; }
  .box-front--navy .properties { left: 196px; top: 226px; font-size: 12.5px; line-height: 20px; }
  .box-front--umber .properties { left: 12px; top: 226px; font-size: 13.5px; font-weight: 700; line-height: 22px; }

  .weight { position: absolute; color: var(--cream); z-index: 2; }
  .box-front--navy .weight { right: 30px; bottom: 26px; font-family: "Tinos", serif; font-size: 12px; }
  .box-front--umber .weight { left: 14px; bottom: 22px; font-family: "Roboto", sans-serif; font-size: 12px; }

  .wave { position: absolute; left: 0; top: 190px; width: 100%; height: 220px; }

  .photo-vegetables {
    position: absolute; left: 8px; top: 196px; width: 176px; height: 178px; border-radius: 14px;
    background: linear-gradient(160deg, var(--veg-mix) 0%, var(--veg-warm) 100%);
    opacity: .85;
  }

  .accent-circle {
    position: absolute; left: 156px; top: 176px; width: 300px; height: 300px; border-radius: 50%;
    background: var(--umber-circle); opacity: .7;
  }
  .photo-pasta-bowl {
    position: absolute; left: 160px; top: 200px; width: 166px; height: 176px; border-radius: 14px;
    background: linear-gradient(160deg, var(--pasta) 0%, var(--pasta-deep) 100%);
  }
  .photo-pasta-small {
    position: absolute; left: 266px; top: 140px; width: 60px; height: 52px; border-radius: 10px;
    background: linear-gradient(160deg, var(--pasta) 0%, var(--pasta-deep) 100%);
  }
</style>
</head>
<body>
<div class="canvas">

  <section class="box-front box-front--navy">
    <div class="label-band"></div>
    <div class="label-frame">
      <svg class="wave" viewBox="0 0 330 220" preserveAspectRatio="none" aria-hidden="true">
        <path d="M0 60 Q60 0 150 10 Q200 14 230 30 Q280 10 330 60 L330 220 L0 220 Z" fill="var(--navy-wave)"/>
      </svg>
      <div class="brand">KORNIVA</div>
      <h1 class="product-name">FUSILLI</h1>
      <div class="photo-vegetables" role="img" aria-label="Foto: frisches Gemüse, Getreideähren und eine Schale Buchweizen-Fusilli"></div>
      <ul class="properties">
        <li>Eigenschaften:</li>
        <li>- Buchweizenmehl</li>
        <li>- 100% Vegan</li>
        <li>- Kochzeit 3 Minuten</li>
        <li>- Liebevolle Handarbeit</li>
      </ul>
      <p class="weight">Produktgewicht: 250g</p>
    </div>
  </section>

  <section class="box-front box-front--umber">
    <div class="label-band"></div>
    <div class="label-frame">
      <div class="accent-circle"></div>
      <div class="photo-pasta-bowl" role="img" aria-label="Foto: Holzschale mit Fusilli, von oben"></div>
      <div class="photo-pasta-small" role="img" aria-label="Foto: kleine Holzschale mit Fusilli"></div>
      <div class="brand">KORNIVA</div>
      <h1 class="product-name">FUSILLI</h1>
      <ul class="properties">
        <li>Eigenschaften:</li>
        <li>- Buchweizenmehl</li>
        <li>- 100% Vegan</li>
        <li>- Kochzeit 3 Minuten</li>
        <li>- Liebevolle Handarbeit</li>
      </ul>
      <p class="weight">Produktgewicht: 250g</p>
    </div>
  </section>

</div>
</body>
</html>
```